BRIVETTA Need a luxury modern business card designed.

Need a luxury modern business card designed. refer to the uploaded files for the company name and logo in the zip file under source files. i will making my descion on monday. so please send in before then so if we need to edit we will have the time. we have a trade show coming up and im on a deadline for printer.

Target Market(s)

high end clients

Contact Information for Business Card

Company nAme and logo. Calvin Moross Co-Founder / Project Manager Office # 416-555-7391 Cell # 416-555-0186 BRIVETTA.CA Calvin@brivetta.ca

Font styles to use
Other font styles liked:
• Modern

Requirements
Must have
• Company name and logo, contact info, using the black, gold and white color scheme.

```html
<!DOCTYPE html>
<html lang="en">
<head>
<meta charset="utf-8">
<title>BRIVETTA Business Card</title>
<link rel="stylesheet" href="https://fonts.googleapis.com/css2?family=Rubik:wght@400;500;700&family=Josefin+Sans:wght@300&display=swap">
<style>
  :root {
    --backdrop: #9a9a9a;
    --card: #2e2e2e;
    --card-back: #2a2a28;
    --pattern-tone: #3a3830;
    --gold: #a8925a;
    --white: #f2f2f2;
    --shadow: rgba(0,0,0,0.35);
  }
  * { margin: 0; padding: 0; box-sizing: border-box; }
  html, body { width: 1200px; height: 1021px; overflow: hidden; }
  body {
    background: var(--backdrop);
    font-family: "Rubik", sans-serif;
    position: relative;
  }
  .card {
    position: absolute;
    left: 190px;
    width: 820px;
    height: 468px;
    border-radius: 4px;
    box-shadow: 0 10px 28px var(--shadow);
    overflow: hidden;
  }
  .card-back { top: 28px; background: var(--card-back); }
  .card-front { top: 525px; background: var(--card); }

  .back-pattern {
    position: absolute;
    inset: 0;
    background: linear-gradient(135deg, var(--card-back) 0%, var(--pattern-tone) 50%, var(--card-back) 100%);
  }
  .back-brand {
    position: absolute;
    right: 48px;
    bottom: 44px;
    font-family: "Josefin Sans", sans-serif;
    font-weight: 300;
    font-size: 26px;
    letter-spacing: 6px;
    color: var(--white);
  }

  .brand-lockup {
    position: absolute;
    left: 60px;
    top: 150px;
    width: 330px;
    display: flex;
    align-items: center;
    gap: 16px;
  }
  .brand-mark {
    width: 22px;
    height: 22px;
    background: var(--gold);
    flex: none;
  }
  .brand-name {
    font-family: "Josefin Sans", sans-serif;
    font-weight: 300;
    font-size: 44px;
    letter-spacing: 9px;
    color: var(--white);
  }

  .person {
    position: absolute;
    left: 450px;
    top: 150px;
  }
  .person-name {
    color: var(--gold);
    font-weight: 700;
    font-size: 26px;
  }
  .person-title {
    color: var(--white);
    font-weight: 400;
    font-size: 21px;
    margin-top: 4px;
  }
  .divider {
    position: absolute;
    left: 430px;
    right: 0;
    top: 262px;
    height: 2px;
    background: var(--gold);
  }
  .contacts {
    position: absolute;
    left: 440px;
    top: 300px;
    list-style: none;
  }
  .contacts li {
    display: flex;
    align-items: center;
    gap: 10px;
    color: var(--white);
    font-size: 21px;
    line-height: 30px;
  }
  .contacts svg { width: 18px; height: 18px; flex: none; }
</style>
</head>
<body>
  <section class="card card-back">
    <div class="back-pattern" role="img" aria-label="Repeating diagonal brand monogram pattern in dark gold on charcoal"></div>
    <div class="back-brand">BRIVETTA</div>
  </section>

  <section class="card card-front">
    <div class="brand-lockup">
      <span class="brand-mark"></span>
      <span class="brand-name">BRIVETTA</span>
    </div>

    <div class="person">
      <div class="person-name">Calvin Moross</div>
      <div class="person-title">Co-Founder / Project Manager</div>
    </div>
    <div class="divider"></div>

    <ul class="contacts">
      <li>
        <svg viewBox="0 0 24 24" fill="#a8925a"><path d="M6.6 10.8a15 15 0 0 0 6.6 6.6l2.2-2.2c.3-.3.7-.4 1-.2 1.1.4 2.3.6 3.6.6.6 0 1 .4 1 1V20c0 .6-.4 1-1 1A17 17 0 0 1 3 4c0-.6.4-1 1-1h3.5c.6 0 1 .4 1 1 0 1.3.2 2.5.6 3.6.1.3 0 .7-.2 1z"/></svg>
        416-555-7391
      </li>
      <li>
        <svg viewBox="0 0 24 24" fill="none" stroke="#a8925a" stroke-width="2"><rect x="6" y="2" width="12" height="20" rx="2"/><line x1="11" y1="18" x2="13" y2="18"/></svg>
        416-555-0186
      </li>
      <li>
        <svg viewBox="0 0 24 24" fill="none" stroke="#a8925a" stroke-width="2"><rect x="2" y="5" width="20" height="14"/><polyline points="2,5 12,13 22,5"/></svg>
        Calvin@brivetta.ca
      </li>
      <li>
        <svg viewBox="0 0 24 24" fill="none" stroke="#a8925a" stroke-width="2"><circle cx="12" cy="12" r="10"/><ellipse cx="12" cy="12" rx="4" ry="10"/><line x1="2" y1="12" x2="22" y2="12"/></svg>
        BRIVETTA.CA
      </li>
    </ul>
  </section>
</body>
</html>
```